Buch-/eBook-Cover für Traumatherapeutin
Zielgruppe
Ich bin Traumatherapeutin und schreibe ein Buch zum Thema Trauma bearbeiten.
Meine Zielgruppe sucht Heilung, Genesung, Selbstliebe etc.
Aufgabenstellung
Buchcover
Bitte erstell mir ein modernes positives inspirierendes Buchcover mit dem
Titel: 'Morgens LEISE aufbrechen“
Untertitel: „Geh den Pfad, der dich leise ruft“
Dr. Merle Kuhnast
Ich hätte gerne ein modernes Buch, das entweder einen Bezug zum Thema Trauma hat oder aber einfach stylische Schriftzüge. Bin aber auch offen für andere Vorschläge.
Dunkelblau, weiß und türkis oder auch rosa mag ich ganz gerne. Wobei Dunkelblau, weiß und türkis meine Favoriten sind und mit rosa höchstens kleinere Akzente gesetzt werden sollten.
Das Buchcover soll modern sein und direkt ansprechen. Gerne eine originelle Lösung, oder etwas Besonderes, etwas das Tiefe ausdrückt, oder man mehrmals hinsehen muss um etwas zu erkennen oder etwas das mehr Interpretationsspielraum lässt.
Gerne auch viel weiß, zumindest heller und nicht zu dunkel. Stylish, aber nicht überfrachtet.
Schreib mich gerne an, wenn du Fragen hast.
Ich habe mal zwei Beispiel von Typolösungen angehängt, die ich ganz cool fände.
Ich freue mich auf deine Ideen :-)
Ganz liebe Grüße
Merle

```html
<!DOCTYPE html>
<html lang="de">
<head>
<meta charset="utf-8">
<title>Morgens leise aufbrechen – Dr. Merle Kuhnast</title>
<link rel="stylesheet" href="https://fonts.googleapis.com/css2?family=Montserrat:wght@800&family=Source+Sans+3:wght@400&family=Dancing+Script:wght@700&family=Yellowtail&display=swap">
<style>
  :root {
    --surround: #676767;
    --paper: #ffffff;
    --navy: #156a9c;
    --title-blue: #7ab7d7;
    --script-light: #6aaccf;
    --wash-light: #e3f3fa;
    --wash-mid: #b5e0f0;
    --wash-deep: #8fd0e8;
    --dots: #4a97bd;
  }
  html, body {
    margin: 0;
    padding: 0;
    width: 881px;
    height: 1200px;
    overflow: hidden;
    background: var(--surround);
  }
  .canvas {
    position: relative;
    width: 881px;
    height: 1200px;
    background: var(--surround);
  }
  .cover {
    position: absolute;
    left: 83px;
    top: 76px;
    width: 716px;
    height: 1016px;
    background: var(--paper);
    overflow: hidden;
  }
  .author {
    position: absolute;
    top: 89px;
    left: 0;
    width: 100%;
    text-align: center;
    font-family: "Source Sans 3", sans-serif;
    font-size: 37px;
    letter-spacing: 1px;
    color: var(--navy);
    text-transform: uppercase;
  }
  .wash {
    position: absolute;
    left: 0;
    top: 200px;
    width: 716px;
    height: 494px;
    border-radius: 42% 38% 45% 40% / 45% 40% 48% 42%;
    background:
      radial-gradient(ellipse at 55% 45%, var(--wash-light) 0%, transparent 55%),
      radial-gradient(ellipse at 30% 55%, var(--wash-mid) 0%, transparent 65%),
      linear-gradient(150deg, var(--wash-deep) 0%, var(--wash-mid) 45%, var(--wash-light) 75%, var(--wash-mid) 100%);
    filter: blur(3px);
  }
  .title {
    position: absolute;
    left: 0;
    top: 0;
    width: 100%;
    margin: 0;
    text-align: center;
    font-weight: normal;
  }
  .title-line {
    position: absolute;
    left: 0;
    width: 100%;
    text-align: center;
    line-height: 1;
  }
  .title-caps {
    font-family: "Montserrat", sans-serif;
    font-weight: 800;
    text-transform: uppercase;
    color: var(--title-blue);
    -webkit-text-stroke: 3px var(--paper);
    paint-order: stroke fill;
  }
  .title-first { top: 256px; font-size: 94px; }
  .title-script {
    top: 355px;
    font-family: "Dancing Script", cursive;
    font-weight: 700;
    font-size: 148px;
    color: var(--navy);
  }
  .title-last { top: 514px; font-size: 88px; letter-spacing: -1px; }
  .subtitle {
    position: absolute;
    top: 778px;
    left: 0;
    width: 100%;
    margin: 0;
    text-align: center;
    font-family: "Source Sans 3", sans-serif;
    font-size: 34px;
    line-height: 48px;
    color: var(--navy);
  }
  .subtitle-accent {
    font-family: "Yellowtail", cursive;
    font-size: 56px;
    color: var(--script-light);
  }
  .path-dots {
    position: absolute;
    left: 0;
    top: 0;
    width: 716px;
    height: 1016px;
  }
</style>
</head>
<body>
  <div class="canvas">
    <div class="cover">
      <div class="author">Dr. Merle Kuhnast</div>

      <div class="wash" role="img" aria-label="Türkisblaue Aquarell-Fläche mit weichen Pinselschwüngen hinter dem Titel"></div>

      <h1 class="title">
        <span class="title-line title-caps title-first">Morgens</span>
        <span class="title-line title-script">leise</span>
        <span class="title-line title-caps title-last">aufbrechen</span>
      </h1>

      <p class="subtitle">Geh den <span class="subtitle-accent">Pfad,</span><br>der dich leise ruft!</p>

      <svg class="path-dots" viewBox="0 0 716 1016" aria-hidden="true">
        <path d="M716 740 Q540 800 475 1016" fill="none" stroke="var(--dots)" stroke-width="4.5" stroke-linecap="round" stroke-dasharray="0 8.5"/>
      </svg>
    </div>
  </div>
</body>
</html>
```